Design a Shirt Hang Tag for a brand new streetwear company

We need a hang tag for our apparel. This will be attached and shipper with every shirt, hat, and hoodie. We make streetwear/urban apparel. For a feel of our products see http://loomferal.co

We'd like to see something die cut with a shape that isn't a rectangle.
Looking for a design that embodies "Savage". We are looking for something bold and fun. Our colors usually consist of black. white, and red, but if you feel like doing something else that you feel could fit our brand,go for it. Were savage, we don't want normal.

Target Market(s)

inner city, age 13-29, multi-cultural

Industry/Entity Type

Clothing

Font styles to use
Sans Serif
Other font styles liked:
• artist's choice

Colors
ec1f27
ffffff
000000

Requirements
Must have
• site url: www.loomferal.co
• Band Name: Loom Feral
• Double sided tag
• Die cut design

```html
<!DOCTYPE html>
<html lang="en">
<head>
<meta charset="utf-8">
<title>Loom Feral Hang Tag</title>
<link rel="stylesheet" href="https://fonts.googleapis.com/css2?family=Orbitron:wght@900&family=Pathway+Gothic+One&display=swap">
<style>
  :root {
    --paper: #ffffff;
    --ink: #000000;
    --leaf-deep: #b3280c;
    --leaf-mid: #e8780a;
    --leaf-light: #f6c20d;
    --leaf-glow: #fbe23a;
  }
  * { margin: 0; padding: 0; box-sizing: border-box; }
  html, body { width: 966px; height: 1200px; overflow: hidden; background: var(--paper); }
  .canvas { position: relative; width: 966px; height: 1200px; }

  .tag { position: absolute; left: 86px; width: 794px; height: 351px; }
  .tag--front { top: 143px; }
  .tag--back { top: 541px; }

  .tag__texture {
    position: absolute; inset: 0; border-radius: 24px;
    background:
      radial-gradient(ellipse at 70% 40%, var(--leaf-glow) 0%, transparent 55%),
      linear-gradient(135deg, var(--leaf-deep) 0%, var(--leaf-mid) 18%, var(--leaf-light) 45%, var(--leaf-light) 70%, var(--leaf-mid) 88%, var(--leaf-deep) 100%);
  }
  .tag__frame {
    position: absolute; left: 67px; top: 61px; width: 689px; height: 266px;
    border: 3px solid var(--paper); border-radius: 26px;
  }
  .tag__panel {
    position: absolute; left: 33px; top: 28px; width: 689px; height: 264px;
    background: var(--paper); border-radius: 28px;
  }
  .tag__url {
    position: absolute; left: 211px; bottom: 29px;
    font-family: "Pathway Gothic One", sans-serif; font-size: 27px; line-height: 1;
    color: var(--ink); letter-spacing: 0.5px; white-space: nowrap;
  }

  .wordmark {
    position: absolute; inset: 0; margin: 0;
    font-family: "Orbitron", sans-serif; font-weight: 900; color: var(--ink);
    line-height: 1; white-space: nowrap;
  }
  .wordmark span { position: absolute; display: block; }

  .tag--front .wordmark__top { left: 44px; top: 14px; font-size: 62px; letter-spacing: 2px; }
  .tag--front .wordmark__main { left: 28px; top: 68px; font-size: 126px; letter-spacing: 1px; }

  .tag--back .wordmark__top { left: 28px; top: 22px; font-size: 40px; letter-spacing: 1px; }
  .tag--back .wordmark__main { left: 18px; top: 55px; font-size: 80px; }

  .tag__label-block {
    position: absolute; left: 406px; top: 41px; width: 259px; height: 193px;
    background: var(--ink); border-radius: 26px;
  }
</style>
</head>
<body>
<main class="canvas">
  <section class="tag tag--front">
    <div class="tag__texture" role="img" aria-label="Close-up autumn leaf texture in orange, yellow and deep red"></div>
    <div class="tag__frame"></div>
    <div class="tag__panel">
      <h1 class="wordmark"><span class="wordmark__top">LOOM</span><span class="wordmark__main">FERAL</span></h1>
    </div>
    <p class="tag__url">www.loomferal.co</p>
  </section>

  <section class="tag tag--back">
    <div class="tag__texture" role="img" aria-label="Close-up autumn leaf texture in orange, yellow and deep red"></div>
    <div class="tag__frame"></div>
    <div class="tag__panel">
      <h2 class="wordmark"><span class="wordmark__top">LOOM</span><span class="wordmark__main">FERAL</span></h2>
      <div class="tag__label-block"></div>
    </div>
    <p class="tag__url">www.loomferal.co</p>
  </section>
</main>
</body>
</html>
```